Modern Innovative Business Card Design

We require a nice, modern, clean business card design, ready for upload to Cardomora. Our company develops online banking software solutions for small financial insitutions. The design should be clean, professional, but yet not "corporate boring". See www.fyrolt.com for an idea of business image and profile. The design should communicate innovation, be modern and fresh, yet look professional and established.

Target Market(s)

Finance industry, bankers, entrepreneurs

Industry/Entity Type

Financial

Contact Information for Business Card

Tobias Wendlerup
CEO

FYROLT BV
Lindenwerf 38
1027 HX Amsterdam
The Netherlands

Phone: +31 20 517 8036
Direct: +31 20 604 1758
Skype: tobias.fyrolt
ceo@fyrolt.com
www.fyrolt.com

Font styles to use
Sans Serif

Requirements
Must have
• Should look clean, modern and professional. File should be ready for upload to cardomora.
Should not have
• Boring standard corporate layout

```html
<!DOCTYPE html>
<html lang="en">
<head>
<meta charset="utf-8">
<title>FYROLT Business Card</title>
<link rel="stylesheet" href="https://fonts.googleapis.com/css2?family=Arimo:wght@400;700&display=swap">
<style>
  :root {
    --page-bg: #e4e4e4;
    --card-bg: #ffffff;
    --brand-green: #6fce2f;
    --brand-grey: #555557;
    --text-grey: #4d4d4f;
    --white: #ffffff;
  }
  * { box-sizing: border-box; margin: 0; padding: 0; }
  html, body {
    width: 1200px;
    height: 1159px;
    overflow: hidden;
    background: var(--page-bg);
    font-family: "Arimo", Arial, sans-serif;
  }
  .card {
    position: absolute;
    left: 330px;
    top: 162px;
    width: 540px;
    height: 835px;
    background: var(--card-bg);
    box-shadow: 0 6px 24px rgba(0,0,0,0.12);
    overflow: hidden;
  }
  .wordmark {
    position: absolute;
    left: 56px;
    top: 78px;
    font-size: 82px;
    font-weight: 400;
    letter-spacing: 2px;
    color: var(--brand-grey);
    line-height: 1;
  }
  .website {
    position: absolute;
    left: 196px;
    top: 170px;
    font-size: 22px;
    color: var(--text-grey);
  }
  .name-band {
    position: absolute;
    left: 150px;
    top: 228px;
    width: 390px;
    height: 62px;
    background: var(--brand-grey);
    clip-path: polygon(22px 0, 100% 0, 100% 100%, 0 100%);
  }
  .name-band-tab {
    position: absolute;
    right: 0;
    top: 0;
    width: 30px;
    height: 100%;
    background: var(--brand-green);
  }
  .name {
    position: absolute;
    left: 34px;
    top: 15px;
    font-size: 30px;
    font-weight: 700;
    color: var(--white);
    white-space: nowrap;
  }
  .title-accent {
    position: absolute;
    left: 112px;
    top: 290px;
    width: 24px;
    height: 56px;
    background: var(--brand-grey);
  }
  .title-band {
    position: absolute;
    left: 136px;
    top: 290px;
    width: 262px;
    height: 42px;
    background: var(--brand-green);
    clip-path: polygon(0 0, 100% 0, calc(100% - 18px) 100%, 0 100%);
  }
  .title {
    position: absolute;
    left: 22px;
    top: 11px;
    font-size: 19px;
    font-weight: 700;
    color: var(--white);
    white-space: nowrap;
  }
  .side-bar {
    position: absolute;
    left: 40px;
    top: 430px;
    width: 22px;
    height: 405px;
    background: linear-gradient(var(--brand-green) 0 74%, var(--brand-grey) 74% 100%);
  }
  .contacts {
    position: absolute;
    left: 100px;
    top: 452px;
    list-style: none;
  }
  .contact {
    display: flex;
    align-items: flex-start;
    gap: 16px;
    height: 74px;
    font-size: 24px;
    color: var(--text-grey);
    line-height: 30px;
    white-space: nowrap;
  }
  .contact-icon {
    flex: none;
    width: 38px;
    height: 38px;
    border-radius: 7px;
    background: var(--brand-green);
    display: flex;
    align-items: center;
    justify-content: center;
    margin-top: -3px;
  }
  .contact-icon svg { width: 24px; height: 24px; }
  .address-line-2 { display: block; padding-left: 30px; }
</style>
</head>
<body>
  <main class="card">
    <div class="wordmark">FYROLT</div>
    <div class="website">www.fyrolt.com</div>

    <div class="name-band">
      <span class="name">Tobias Wendlerup</span>
      <span class="name-band-tab"></span>
    </div>
    <div class="title-accent"></div>
    <div class="title-band"><span class="title">CEO FYROLT BV</span></div>

    <div class="side-bar"></div>

    <ul class="contacts">
      <li class="contact">
        <span class="contact-icon">
          <svg viewBox="0 0 24 24" aria-hidden="true"><path fill="#fff" d="M6.6 10.8a15.1 15.1 0 0 0 6.6 6.6l2.2-2.2c.3-.3.7-.4 1-.2 1.1.4 2.3.6 3.6.6.6 0 1 .4 1 1V20c0 .6-.4 1-1 1A17 17 0 0 1 3 4c0-.6.4-1 1-1h3.5c.6 0 1 .4 1 1 0 1.3.2 2.5.6 3.6.1.3 0 .7-.2 1z"/></svg>
        </span>
        <span class="contact-text">+31 20 517 8036</span>
      </li>
      <li class="contact">
        <span class="contact-icon">
          <svg viewBox="0 0 24 24" aria-hidden="true"><path fill="#fff" d="M6.6 10.8a15.1 15.1 0 0 0 6.6 6.6l2.2-2.2c.3-.3.7-.4 1-.2 1.1.4 2.3.6 3.6.6.6 0 1 .4 1 1V20c0 .6-.4 1-1 1A17 17 0 0 1 3 4c0-.6.4-1 1-1h3.5c.6 0 1 .4 1 1 0 1.3.2 2.5.6 3.6.1.3 0 .7-.2 1z"/></svg>
        </span>
        <span class="contact-text">(direct)+31 20 604 1758</span>
      </li>
      <li class="contact">
        <span class="contact-icon">
          <svg viewBox="0 0 24 24" aria-hidden="true"><rect x="5" y="5" width="14" height="14" rx="3" fill="none" stroke="#fff" stroke-width="2"/></svg>
        </span>
        <span class="contact-text">tobias.fyrolt ceo@fyrolt.com</span>
      </li>
      <li class="contact">
        <span class="contact-icon">
          <svg viewBox="0 0 24 24" aria-hidden="true"><path fill="none" stroke="#fff" stroke-width="2" stroke-linejoin="round" d="M3 11 12 4l9 7M5 10v10h14V10M10 20v-6h4v6"/></svg>
        </span>
        <span class="contact-text">Lindenwerf 38 1027 HX<span class="address-line-2">Amsterdam The Netherlands</span></span>
      </li>
    </ul>
  </main>
</body>
</html>
```